Postcard Design

Law office.
Details are on the attached pdf file:
NOTE: the following items are to be changed, as follows:
1. price is 799
2. delete "Expires 2-8-13"
3. make "Nevada County's..." into "Northern California's ... "
4. Someplace where it fits nicely, add "Fast, Easy, Done!"
5. Delete "no obligation first visit"
6. That attached pdf was a successful ad so I want to maintain that look GENERALLY, but I'm not stuck on anything in particular. Some freedom to play with it for a perfect ad.
7. I'll attach the revised picture and the logo.

```html
<!DOCTYPE html>
<html lang="en">
<head>
<meta charset="utf-8">
<title>Estate Plans Postcard</title>
<link rel="stylesheet" href="https://fonts.googleapis.com/css2?family=Crimson+Pro:ital,wght@0,400;0,600;0,700;1,400&family=Lato:ital,wght@0,400;0,700;1,400;1,700&display=swap">
<style>
  :root {
    --green: #5b6a2e;
    --orange: #f7941d;
    --ink: #1f1f1f;
    --slate: #3a3a3a;
    --paper: #ffffff;
    --mist: #e6edf3;
    --backdrop: #ece9e4;
  }
  * { margin: 0; padding: 0; box-sizing: border-box; }
  html, body { width: 1200px; height: 825px; overflow: hidden; background: var(--backdrop); }
  .canvas { position: relative; width: 1200px; height: 825px; }
  .postcard {
    position: absolute; left: 117px; top: 65px; width: 966px; height: 695px;
    background: linear-gradient(160deg, var(--paper) 0%, var(--mist) 45%, var(--paper) 70%, var(--mist) 100%);
    overflow: hidden; box-shadow: 0 4px 14px rgba(0,0,0,.18);
  }
  .postcard > * { position: absolute; }
  .edge-art { left: 0; top: 0; width: 966px; height: 695px; }
  .headline-band {
    left: 0; top: 20px; width: 900px; height: 80px; background: var(--green);
    border-top: 5px solid var(--orange); border-bottom: 5px solid var(--orange);
    display: flex; align-items: center; justify-content: center;
    font: 700 38px/1 "Crimson Pro", serif; color: var(--paper); padding-left: 20px;
  }
  .services { left: 0; width: 880px; top: 120px; text-align: center; font: italic 400 34px/1.2 "Lato", sans-serif; color: var(--ink); }
  .price { left: 80px; top: 168px; font: 700 108px/1 "Crimson Pro", serif; color: var(--green); }
  .price-divider { left: 366px; top: 200px; width: 2px; height: 86px; background: var(--ink); }
  .value { left: 398px; top: 184px; font: 700 40px/1 "Crimson Pro", serif; color: var(--green); }
  .tagline { left: 426px; top: 240px; font: italic 400 36px/1 "Lato", sans-serif; color: var(--ink); }
  .protect { left: 46px; top: 318px; font: 700 38px/1 "Crimson Pro", serif; color: var(--slate); }
  .call-pill {
    left: 533px; top: 318px; width: 310px; height: 44px; border-radius: 22px;
    background: var(--orange); border: 2px solid var(--slate);
    display: flex; align-items: center; justify-content: center;
    font: italic 700 25px/1 "Lato", sans-serif; color: var(--green);
  }
  .portrait-frame { left: 45px; top: 381px; width: 187px; height: 237px; background: var(--orange); padding: 10px; }
  .portrait { width: 100%; height: 100%; background: linear-gradient(180deg, #a9adb0 0%, #7d8286 55%, #222 100%); }
  .office { left: 240px; width: 482px; text-align: center; color: var(--ink); font-family: "Crimson Pro", serif; }
  .office-label { top: 402px; font-size: 25px; font-weight: 400; letter-spacing: .5px; }
  .office-name { top: 440px; font-size: 38px; font-weight: 400; color: var(--green); letter-spacing: 1px; }
  .office-phone { top: 496px; font-size: 28px; font-weight: 700; }
  .office-web { top: 545px; font-size: 21px; font-weight: 400; }
  .notary { top: 584px; font: italic 700 29px/1.2 "Lato", sans-serif; color: var(--green); }
  .brand-mark { left: 720px; top: 417px; width: 137px; height: 173px; display: flex; align-items: center; justify-content: center; gap: 8px; font: 700 24px/1 "Crimson Pro", serif; color: var(--ink); }
  .brand-square { width: 14px; height: 14px; background: var(--ink); }
  .since { left: 700px; top: 598px; width: 180px; text-align: center; font: 400 14px/1.3 "Lato", sans-serif; color: var(--ink); }
  .footer-band { left: 0; top: 663px; width: 900px; height: 32px; background: var(--green); }
</style>
</head>
<body>
<div class="canvas">
  <section class="postcard">
    <div class="headline-band">Northern California's Best in Estate Plans</div>
    <div class="footer-band"></div>
    <svg class="edge-art" viewBox="0 0 966 695" aria-hidden="true">
      <path d="M870,0 C840,140 905,360 880,500 C868,580 850,650 835,695 L966,695 L966,0 Z" fill="var(--green)"/>
      <path d="M890,0 C860,140 925,360 900,500 C888,580 870,650 855,695 L966,695 L966,0 Z" fill="var(--paper)"/>
      <path d="M906,0 C876,140 941,360 916,500 C904,580 886,650 871,695 L966,695 L966,0 Z" fill="var(--orange)"/>
    </svg>
    <p class="services">Living Trusts, Wills &amp; All Necessary Documents</p>
    <p class="price">$799</p>
    <div class="price-divider"></div>
    <p class="value">Over $2,000 value</p>
    <p class="tagline">Fast, Easy, Done!</p>
    <p class="protect">Protect Your Loved Ones!</p>
    <p class="call-pill">It’s Easy — Call Now!</p>
    <div class="portrait-frame"><div class="portrait" role="img" aria-label="Portrait photo of the attorney in a dark suit"></div></div>
    <p class="office office-label">THE LAW OFFICE OF</p>
    <p class="office office-name">DANIEL R. MOREAU</p>
    <p class="office office-phone">Call at - 555-0142</p>
    <p class="office office-web">Check me out at: www.DanielMoreau.com</p>
    <p class="office notary">Free Notarization</p>
    <div class="brand-mark"><span class="brand-square"></span><span>Moreau Law</span></div>
    <p class="since">Thousands Served<br>Since 1998</p>
  </section>
</div>
</body>
</html>
```